Corsets, Cups and Commerce needs a book cover

I've been in lingerie business for 12 years, we own 5 x Lingerie stores. This is my story aimed at women in business or women who want to start a business. Essentially its a business book but also offers bra fitting advice. Although the book cover can be a bit cheeky it also needs to be tasteful. I do not have a colour in mind I just don't like it too girly. I like strong and bold with a feminine touch. The title needs to catch peoples attention when surrounded by so many other books. It needs to have some sort of image or texture. That could be a lace background texture. I like the idea of a bra hanging off the letters or some kind of image of a bra but a beautiful lacy bra. I would like the cover to be more beautiful than tacky even though it has the word 'boobs'.
Updates

Hi everyone, some great designs so far. Many of you have made a bra part of the 'Boobs' word. I thought this could work but it doesn't as it covers up the word 'Boobs' too much and I feel this word will catch peoples attention. If any of you would like to revise please feel free. thankyou Delphine.

Target Market(s)

Women in business or women wanting to start a business.

Industry/Entity Type

Retail

Logo Text

Corsets, Cups and Commerce

Font styles to use
Serif
Sans Serif

Colors

Designer to choose colors to be used in the design.

Requirements
Must have
• Title: Corsets, Cups and Commerce (you could replace 'and' with '&' if it works better.
• Tagline: Steady Lessons for Women in Trade
• Author: Delphine Karsby
Nice to have
• An image of a bra, maybe in a playful way. It could hang off the letters or maybe the letters could look like a bra, but I'm concerned it may look tacky that way. Somehow incorporate a picture of a bra preferably as part of the title.
• I don't have images for you, you have the freedom to choose.
Should not have
• Although this book has boobs and bras in the title it must not be tacky or sexual. It is a business book.
• I do not like it to look too girly, probably not script unless its subtle.

```html
<!DOCTYPE html>
<html lang="en">
<head>
<meta charset="utf-8">
<title>Corsets, Cups and Commerce — Book Cover</title>
<link rel="stylesheet" href="https://fonts.googleapis.com/css2?family=Cinzel:wght@400;500&family=Indie+Flower&display=swap">
<style>
  :root {
    --backdrop: #bb8abd;
    --cover-purple: #6b209c;
    --cover-purple-deep: #5a1788;
    --cover-purple-light: #7a2eab;
    --lace-white: #f1e9f6;
    --ink-white: #ffffff;
    --accent-navy: #2c1f6e;
  }
  * { margin: 0; padding: 0; box-sizing: border-box; }
  html, body {
    width: 1200px;
    height: 806px;
    overflow: hidden;
    background: var(--backdrop);
  }
  .stage {
    position: relative;
    width: 1200px;
    height: 806px;
    display: flex;
    align-items: center;
    justify-content: center;
  }
  .book-cover {
    position: relative;
    width: 494px;
    height: 744px;
    background: radial-gradient(ellipse at 50% 40%, var(--cover-purple-light) 0%, var(--cover-purple) 55%, var(--cover-purple-deep) 100%);
    box-shadow: 0 10px 28px rgba(60, 20, 80, 0.35);
    overflow: hidden;
  }
  .lace-corner {
    position: absolute;
    top: 0;
    left: 0;
    width: 240px;
    height: 165px;
  }
  .lace-border {
    position: absolute;
    left: 0;
    bottom: 0;
    width: 494px;
    height: 58px;
  }
  .tagline {
    position: absolute;
    top: 40px;
    right: 78px;
    text-align: right;
    font-family: "Cinzel", serif;
    font-weight: 400;
    font-size: 14px;
    line-height: 18px;
    color: var(--ink-white);
    letter-spacing: 0.3px;
  }
  .title-block {
    position: absolute;
    top: 228px;
    left: 0;
    width: 100%;
    text-align: center;
    color: var(--ink-white);
    font-family: "Cinzel", serif;
  }
  .title-art {
    display: block;
    width: 150px;
    height: 70px;
    margin: 0 auto 4px;
  }
  .title-main {
    display: block;
    font-size: 66px;
    font-weight: 400;
    line-height: 1;
    letter-spacing: 1px;
  }
  .title-sub {
    display: block;
    margin-top: 8px;
    font-size: 30px;
    font-weight: 400;
    line-height: 1;
    letter-spacing: 0.5px;
  }
  .author {
    position: absolute;
    top: 588px;
    left: 0;
    width: 100%;
    text-align: center;
    font-family: "Indie Flower", cursive;
    font-size: 34px;
    color: var(--lace-white);
    word-spacing: 14px;
  }
</style>
</head>
<body>
  <main class="stage">
    <section class="book-cover" aria-label="Book cover: Corsets, Cups and Commerce">
      <svg class="lace-corner" viewBox="0 0 240 165" role="img" aria-label="White lace trim across the top left corner">
        <defs>
          <linearGradient id="laceFade" x1="0" y1="0" x2="1" y2="1">
            <stop offset="0" stop-color="#f1e9f6" stop-opacity="0.85"/>
            <stop offset="1" stop-color="#d9c6e6" stop-opacity="0.55"/>
          </linearGradient>
        </defs>
        <path d="M0 0 H240 Q200 40 150 70 Q90 110 40 140 Q18 154 0 165 Z" fill="url(#laceFade)"/>
      </svg>

      <p class="tagline">Steady Lessons<br>for Women<br>in Trade</p>

      <h1 class="title-block">
        <svg class="title-art" viewBox="0 0 150 70" role="img" aria-label="Navy lace bra illustration set into the title">
          <rect x="0" y="0" width="150" height="70" rx="35" fill="var(--accent-navy)"/>
        </svg>
        <span class="title-main">Corsets</span>
        <span class="title-sub">Cups &amp; Commerce</span>
      </h1>

      <p class="author">Delphine Karsby</p>

      <svg class="lace-border" viewBox="0 0 494 58" preserveAspectRatio="none" role="img" aria-label="White scalloped lace border along the bottom edge">
        <defs>
          <linearGradient id="borderFade" x1="0" y1="0" x2="0" y2="1">
            <stop offset="0" stop-color="#e4d6ee" stop-opacity="0.6"/>
            <stop offset="1" stop-color="#f1e9f6" stop-opacity="0.9"/>
          </linearGradient>
        </defs>
        <path d="M0 58 V34 Q41 4 82 30 Q123 4 165 30 Q206 4 247 30 Q288 4 329 30 Q370 4 412 30 Q453 4 494 34 V58 Z" fill="url(#borderFade)"/>
      </svg>
    </section>
  </main>
</body>
</html>
```